50 Page Catalog Full Redesign New Look

We are looking for a redesign of our Catalog,

We are looking for a modern redesign of our Catalog, with our new logo most of the products will be the same with some new products as well.
Please use colors in the new logo attached
Attached is our current design please see this for what product will go in the catulog
Updates

Designs look the same

Target Market(s)

Automotive

Font styles to use
Other font styles liked:
• Our Font is outfit

Colors

Designer to choose colors to be used in the design.

```html
<!DOCTYPE html>
<html lang="en">
<head>
<meta charset="utf-8">
<title>Norvale Catalogue – Spread</title>
<link href="https://fonts.googleapis.com/css2?family=Outfit:wght@300;400;500;600;700&display=swap" rel="stylesheet">
<style>
  :root{
    --bg:#e5e6e8;
    --paper:#f4f5f6;
    --navy:#1c4676;
    --navy-deep:#173b66;
    --blue:#2f6aa6;
    --ink:#4a5563;
    --gold:#f3b52f;
    --white:#ffffff;
  }
  *{box-sizing:border-box;margin:0;padding:0}
  html,body{width:1200px;height:840px;overflow:hidden}
  body{background:var(--bg);font-family:"Outfit",sans-serif;color:var(--ink)}
  .spread{position:absolute;left:70px;top:45px;width:1060px;height:750px;display:flex;box-shadow:0 10px 30px rgba(0,0,0,.18)}
  .page{position:relative;width:530px;height:750px;overflow:hidden}
  .page--left{background:var(--paper)}
  .page--right{background:linear-gradient(160deg,#22548a,var(--navy-deep))}

  .photo{position:absolute}
  .photo--desk{left:0;top:0;width:530px;height:380px;background:linear-gradient(135deg,#d9d3d6 0%,#e9e2e6 40%,#c9c6c8 70%,#8f98a3 100%)}
  .photo--meeting{left:0;top:440px;width:530px;height:310px;background:linear-gradient(150deg,#7f9bb8 0%,#9fb6cc 35%,#3d5675 75%,#24344d 100%)}

  .feature{position:absolute;border-left:4px solid var(--gold);padding-left:12px}
  .feature--stock{left:34px;top:404px;width:250px}
  .feature--central{left:300px;top:404px;width:205px}
  .feature__title{color:var(--blue);font-weight:700;font-size:19px;line-height:1.15;margin-bottom:10px}
  .feature__text{font-size:10.5px;line-height:1.5;font-weight:400}
  .feature__link{font-weight:700;text-decoration:underline;color:var(--ink)}

  .brand-name{position:absolute;display:flex;align-items:center;gap:8px;font-weight:700;white-space:nowrap}
  .brand-name--instock{left:40px;top:572px;color:var(--blue);font-size:24px}
  .brand-name--portal{left:318px;top:590px;color:var(--navy);font-size:32px}
  .brand-name__mark{width:12px;height:12px;background:currentColor}
  .brand-name__mark--round{border-radius:50%}

  .page__rule{position:absolute;left:34px;right:34px;top:690px;border-top:1px solid #3a3f46}
  .page__footer{position:absolute;left:0;right:0;top:708px;text-align:center;font-size:12px;letter-spacing:.5px;color:#555}

  .values{position:absolute;left:26px;top:40px;display:grid;grid-template-columns:repeat(2,122px);gap:12px}
  .value{height:170px;border:1px solid var(--gold);border-radius:12px;overflow:hidden;background:var(--navy-deep);color:var(--white);text-align:center}
  .value__photo{height:100px}
  .value__photo--care{background:linear-gradient(160deg,#c8d2dc,#7d1f27)}
  .value__photo--speed{background:linear-gradient(160deg,#b3262d,#3a2a30)}
  .value__photo--satisfaction{background:linear-gradient(160deg,#56606b,#1f2730)}
  .value__photo--enjoyment{background:linear-gradient(160deg,#c8d3de,#b52a2e)}
  .value__title{font-size:16px;font-weight:500;margin:8px 0 3px}
  .value__text{font-size:9px;line-height:1.3;padding:0 8px;font-weight:300}

  .about{position:absolute;left:300px;top:44px;width:204px;color:var(--white)}
  .about__title{color:var(--gold);font-weight:700;font-size:20px;margin-bottom:12px}
  .about__text{font-size:9.6px;line-height:1.55;font-weight:300;margin-bottom:10px;text-align:justify}
</style>
</head>
<body>
<main class="spread">
  <section class="page page--left">
    <div class="photo photo--desk" role="img" aria-label="Photo of a smiling woman at a table with a laptop showing the online store, a glass and a small plant"></div>

    <article class="feature feature--stock">
      <h2 class="feature__title">Are You Always Running Out of Stock?</h2>
      <p class="feature__text">Our Instock Solution is the answer to your chaos! Visit <span class="feature__link">norvalepromo.com.au/instock/</span> to find out how we can help you by using our warehouse to store your goods ready for immediate delivery.</p>
    </article>

    <article class="feature feature--central">
      <h2 class="feature__title">Centralised efficiency!</h2>
      <p class="feature__text">Mynorvale is your online promotional one stop shop! View your own products, place orders and browse your past ordering history on <span class="feature__link">norvalepromo.com.au/mynorvale/</span> Reach out to your account manager for a demo.</p>
    </article>

    <p class="brand-name brand-name--instock"><span class="brand-name__mark"></span>Norvale Instock</p>
    <p class="brand-name brand-name--portal"><span class="brand-name__mark brand-name__mark--round"></span>mynorvale</p>

    <div class="page__rule"></div>
    <p class="page__footer">norvale.com.au</p>
  </section>

  <section class="page page--right">
    <div class="values">
      <div class="value">
        <div class="value__photo value__photo--care" role="img" aria-label="Photo of a red heart beside a stopwatch"></div>
        <h3 class="value__title">Care</h3>
        <p class="value__text">Others needs above our own will always result in a win-win.</p>
      </div>
      <div class="value">
        <div class="value__photo value__photo--speed" role="img" aria-label="Photo of a red sports car"></div>
        <h3 class="value__title">Speed</h3>
        <p class="value__text">Efficiency in everything we do</p>
      </div>
      <div class="value">
        <div class="value__photo value__photo--satisfaction" role="img" aria-label="Photo of a luxury car interior and steering wheel"></div>
        <h3 class="value__title">Satisfaction</h3>
        <p class="value__text">Exceeding expectations every time</p>
      </div>
      <div class="value">
        <div class="value__photo value__photo--enjoyment" role="img" aria-label="Photo of a red apple with a measuring tape"></div>
        <h3 class="value__title">Enjoyment</h3>
        <p class="value__text">All with an element of fun.</p>
      </div>
    </div>

    <article class="about">
      <h2 class="about__title">Who we are</h2>
      <p class="about__text">For over three decades, Norvale has provided complete merchandise solutions for an ever-increasing number of Australian corporations and businesses. During this time, our already vast range has grown exponentially and our systems have become increasingly more streamlined to cope with the sheer volume.</p>
      <p class="about__text">Our enviable reputation is built on experience, innovation and economies of scale that come with being a major wholesaler in Australia. We pride ourselves on our accountability, efficiency, consistency, instant reporting and above all, the ability to see things from your point of view.</p>
      <p class="about__text">We love to strategise with you to make sure what we supply will achieve the desired outcome. Every day we see companies giving away merchandise aimlessly and our mission is to supply you with a product that will suit your criteria.</p>
    </article>

    <div class="photo photo--meeting" role="img" aria-label="Photo of a business team meeting in a bright office with a presenter beside a data screen"></div>
  </section>
</main>
</body>
</html>
```